GravaLoop. Customer needs to know about us, what services we provide & contact us

We are a waste tire recycling company. Our primary focus is on providing a sustainable and cost effective service focusing on: Waste Tire Management, Hassle Free Scheduling for Tire Collection, Mobile Shredding & Special site cleanup services. GravaLoop will be producing TDF, Clean Tire Wire & further materials.
Please look at https://harvonrubber.example
Please look at https://quelbamaterials.example

This is the look and feel of what we want

I have attached a word document with our website info.

Target Market(s)

Tire Install Companies. Such as morbanhaul.example. TDF Purchasers such as pelkofuel.example.

Industry/Entity Type

Waste Tire Recycling

Coding

Coded - Design and coding required

Number of Pages Required

3 page

Font styles to use
Other font styles liked:
• Look at our logo

Requirements
Must have
• We need a 3 page setup for About Us, Services & Contact Us. Contact us should be a form them can fill out and submit to us Images that are related to waste tire recycling. Clean, modern, innovative.
Nice to have
• The color and feel of the website should work with our logo that we did with artpivot
Should not have
• Anything progressive, political or "woke"

```html
<!DOCTYPE html>
<html lang="en">
<head>
<meta charset="utf-8">
<title>GravaLoop – Waste Tire Recycling</title>
<link rel="stylesheet" href="https://fonts.googleapis.com/css2?family=Exo+2:ital,wght@1,800&family=Open+Sans:wght@400;600&family=Roboto:wght@400;500&display=swap">
<style>
:root{
  --green:#0f9141;
  --green-dark:#0a7a35;
  --green-band:#5fb97c;
  --ink:#1b1b1b;
  --text:#3d3d3d;
  --muted:#f2f2f2;
  --footer:#2b2b2b;
  --footer-band:#8c8c8c;
  --hero-band:#cdc7bf;
  --footer-line:#4a4a4a;
  --white:#ffffff;
}
*{margin:0;padding:0;box-sizing:border-box}
html,body{width:1200px;height:3976px;overflow:hidden}
body{position:relative;background:var(--white);font-family:"Open Sans",sans-serif;color:var(--text)}
.abs{position:absolute}
/* header */
.site-header{left:0;top:0;width:1200px;height:108px;background:var(--white)}
.brand{left:116px;top:34px;font:600 34px/1 "Open Sans",sans-serif;color:var(--green-dark);letter-spacing:-.5px}
.nav{left:452px;top:43px;font-size:17px;color:var(--ink)}
.nav a{position:absolute;white-space:nowrap;text-decoration:none;color:inherit}
.nav a.active{color:var(--green);font-weight:600}
.btn{display:flex;align-items:center;justify-content:center;border-radius:10px;font-weight:600;text-decoration:none}
.btn-quote{left:946px;top:29px;width:142px;height:51px;background:var(--green);color:var(--white);font-size:17px;border-radius:12px}
/* hero */
.hero-photo{left:0;top:108px;width:1200px;height:650px;background:linear-gradient(180deg,#b9c3c9 0%,#8b8f8f 35%,#4c4945 65%,#6e655c 100%)}
.hero-divider{left:0;top:716px;width:1200px;height:42px;background:var(--hero-band)}
.hero-ring{left:340px;top:160px;width:520px;height:520px;border-radius:50%;border:3px solid var(--green)}
.hero-circle{left:350px;top:170px;width:500px;height:500px;border-radius:50%;background:rgba(15,145,65,.93);text-align:center;color:var(--white)}
.hero-kicker{position:absolute;left:0;right:0;top:112px;font-size:29px}
.hero-title{position:absolute;left:0;right:0;top:150px;font:800 italic 48px/1 "Exo 2",sans-serif}
.hero-text{position:absolute;left:40px;right:40px;top:222px;font-size:16px;line-height:30px}
.btn-outline{position:absolute;left:178px;top:333px;width:144px;height:54px;border:2px solid var(--white);border-radius:12px;color:var(--white);font-size:17px}
/* section heading */
.heading{font:800 italic 40px/1 "Exo 2",sans-serif;color:var(--ink);white-space:nowrap}
.heading em{color:var(--green);font-style:inherit}
/* about */
.about-art{left:70px;top:826px;width:416px;height:486px;border-radius:50%/40%;background:radial-gradient(ellipse at 50% 40%,#3fbf5c 0%,#1e9a3c 45%,#ffffff 75%)}
.about-title{left:551px;top:900px}
.about-text{left:551px;top:958px;width:537px;font-size:16.5px;line-height:30px;text-align:justify}
.btn-green{background:var(--green);color:var(--white);font-size:17px;border-radius:12px}
.about-btn{left:551px;top:1186px;width:142px;height:50px}
/* services */
.services{left:0;top:1351px;width:1200px;height:780px;background:var(--green)}
.section-divider{left:0;width:1200px;height:56px;background:var(--green-band)}
.services-title{left:0;width:1200px;top:1464px;text-align:center}
.service{width:240px;text-align:center;color:var(--white);font-family:"Roboto",sans-serif}
.service.is-active{background:var(--muted);color:var(--ink)}
.service-photo{position:absolute;left:29px;width:182px;height:182px;border-radius:50%;border:3px solid var(--white)}
.service h3{position:absolute;left:0;right:0;font-weight:500;font-size:19px;line-height:28px}
.service p{position:absolute;left:18px;right:18px;font-size:16.5px;line-height:28.5px}
.chevron{position:absolute;left:104px;width:32px;height:32px}
/* produce */
.produce-title{left:0;width:1200px;top:2213px;text-align:center}
.product{width:459px;height:278px;border-radius:40px;overflow:hidden}
.product-photo{position:absolute;inset:0}
.product-bar{position:absolute;left:0;right:0;bottom:0;height:86px;background:var(--green);color:var(--white);font:800 italic 18px/26px "Exo 2",sans-serif;display:flex;align-items:center;padding-left:36px}
.product-bar svg{position:absolute;right:40px;top:30px}
/* blog */
.blog{left:0;top:2690px;width:1200px;height:750px;background:var(--muted)}
.blog-title{left:0;width:1200px;top:2759px;text-align:center}
.post{width:315px;height:480px;background:var(--white);border:1px solid #d6d6d6;border-radius:6px;overflow:hidden;font-family:"Roboto",sans-serif}
.post-photo{position:absolute;left:0;top:0;width:100%;height:206px}
.post-date{position:absolute;right:18px;top:24px;width:60px;height:60px;border-radius:50%;background:var(--green);color:var(--white);font-size:16px;line-height:19px;text-align:center;padding-top:11px}
.post h4{position:absolute;left:22px;right:40px;top:241px;font-weight:500;font-size:16.5px;line-height:26px;color:var(--ink)}
.post .tag{position:absolute;left:22px;top:302px;font-size:16.5px;color:var(--green)}
.post p{position:absolute;left:22px;right:44px;top:338px;font-size:16px;line-height:26px;color:var(--text)}
/* footer */
.footer-divider{left:0;top:3435px;width:1200px;height:62px;background:var(--footer-band)}
.footer{left:0;top:3497px;width:1200px;height:479px;background:var(--footer);color:var(--white)}
.footer-brand{left:111px;top:3560px;font:600 40px/1 "Open Sans",sans-serif;color:var(--white)}
.subscribe{left:661px;top:3556px;width:427px;height:57px;background:var(--white);border:2px solid var(--white);border-radius:12px}
.subscribe span{position:absolute;left:20px;top:17px;font-size:16px;color:#555}
.subscribe b{position:absolute;right:0;top:0;width:145px;height:53px;border-radius:10px;background:var(--green);color:var(--white);font-weight:400;font-size:18px;display:flex;align-items:center;justify-content:center}
.rule{background:var(--footer-line);height:1px}
.vrule{background:var(--footer-line);width:1px;top:3678px;height:210px}
.col-title{font:500 16.5px/1 "Roboto",sans-serif;text-transform:uppercase;top:3686px;color:var(--white)}
.links{list-style:none;font-size:15.5px;line-height:30px;top:3720px;color:var(--white)}
.links li{padding-left:26px;position:relative}
.links li::before{content:"";position:absolute;left:4px;top:11px;width:6px;height:6px;border-right:1.5px solid var(--green);border-top:1.5px solid var(--green);transform:rotate(45deg)}
.contact-line{font-size:15.5px;line-height:27px;color:var(--white)}
.social{left:994px;width:40px;height:40px;border:2px solid var(--white);border-radius:50%}
.copyright{left:0;width:1200px;top:3941px;text-align:center;font-size:15.5px;color:var(--white)}
</style>
</head>
<body>

<header class="abs site-header">
  <div class="abs brand">GravaLoop</div>
  <nav class="abs nav">
    <a class="active" style="left:0">Home</a>
    <a style="left:82px">About</a>
    <a style="left:166px">Services</a>
    <a style="left:267px">We Provide</a>
    <a style="left:395px">Contact</a>
  </nav>
  <a class="abs btn btn-quote">Get a Quote</a>
</header>

<section>
  <div class="abs hero-photo" role="img" aria-label="Stacked used truck tires beside a large pile of shredded tire rubber under a steel shed"></div>
  <div class="abs hero-divider"></div>
  <div class="abs hero-ring"></div>
  <div class="abs hero-circle">
    <div class="hero-kicker">Welcome to</div>
    <h1 class="hero-title">GravaLoop</h1>
    <p class="hero-text">Nemo enim ipsam voluptatem quia voluptas sit aspernatur aut odit aut fugit, sed quia consequuntur magni dolores</p>
    <a class="btn btn-outline">Learn More</a>
  </div>
</section>

<section>
  <div class="abs about-art" role="img" aria-label="Tire and alloy wheel wrapped by three green recycling arrows"></div>
  <h2 class="abs heading about-title"><em>About</em> Us</h2>
  <p class="abs about-text">Nemo enim ipsam voluptatem quia voluptas sit aspernatur aut odit aut fugit, sed quia consequuntur magni dolores eos qui ra voluptatem sequi nesciunt. Neque porro quisquam est, qui dolorem ipsum dolor sit amet, consectetur, adipisci velit, sed quia non numquam eius modi tempora incidunt ut labore et dolore magnam aliquam qt voluptatem. Ut enim ad minima veniam, quis nostrum exercitationem um corporis suscipit laboriosam.</p>
  <a class="abs btn btn-green about-btn">Learn More</a>
</section>

<section>
  <div class="abs services"></div>
  <div class="abs section-divider" style="top:1351px"></div>
  <div class="abs section-divider" style="top:2075px"></div>
  <div class="abs services-title"><h2 class="heading"><em style="color:var(--white)">Our</em> Services</h2></div>

  <div class="abs service" style="left:110px;top:1581px;height:340px">
    <div class="service-photo" style="top:0;background:radial-gradient(circle,#555 0%,#1d1d1d 70%)" role="img" aria-label="Stack of used car tires"></div>
    <h3 style="top:206px">Waste Tire<br>Management</h3>
    <p style="top:276px">Nemo enim ipsamitr dolo voluptatem quia voluptas sit asperna lorem soloris</p>
    <svg class="chevron" style="top:385px" viewBox="0 0 32 32"><circle cx="16" cy="16" r="15" fill="#fff"/><path d="M10 13l6 6 6-6" fill="none" stroke="#0f9141" stroke-width="2.5"/></svg>
  </div>

  <div class="abs service is-active" style="left:357px;top:1663px;height:321px">
    <div class="service-photo" style="top:-82px;background:radial-gradient(circle,#e7d6c8 0%,#8e7f76 75%)" role="img" aria-label="Hands holding a smartphone to book a pickup"></div>
    <h3 style="top:124px">Hassle Free<br>Scheduling</h3>
    <p style="top:194px">Nemo enim ipsamitr dolo voluptatem quia voluptas sit asperna lorem soloris</p>
    <svg class="chevron" style="top:303px" viewBox="0 0 32 32"><circle cx="16" cy="16" r="14" fill="#0f9141" stroke="#fff" stroke-width="2"/><path d="M10 13l6 6 6-6" fill="none" stroke="#fff" stroke-width="2.5"/></svg>
  </div>

  <div class="abs service" style="left:603px;top:1581px;height:340px">
    <div class="service-photo" style="top:0;background:radial-gradient(circle,#6f7680 0%,#2b3037 60%,#2f6fb0 100%)" role="img" aria-label="Gloved hand holding shredded tire pieces"></div>
    <h3 style="top:206px">Mobile Shredding<br>services</h3>
    <p style="top:276px">Nemo enim ipsamitr dolo voluptatem quia voluptas sit asperna lorem soloris</p>
    <svg class="chevron" style="top:385px" viewBox="0 0 32 32"><circle cx="16" cy="16" r="15" fill="#fff"/><path d="M10 13l6 6 6-6" fill="none" stroke="#0f9141" stroke-width="2.5"/></svg>
  </div>

  <div class="abs service" style="left:848px;top:1581px;height:340px">
    <div class="service-photo" style="top:0;background:linear-gradient(180deg,#d7dde2 0%,#9a958d 45%,#4a463f 100%)" role="img" aria-label="Excavator clearing a large site of scrap tires"></div>
    <h3 style="top:206px">Special site cleanup<br>services</h3>
    <p style="top:276px">Nemo enim ipsamitr dolo voluptatem quia voluptas sit asperna lorem soloris</p>
    <svg class="chevron" style="top:385px" viewBox="0 0 32 32"><circle cx="16" cy="16" r="15" fill="#fff"/><path d="M10 13l6 6 6-6" fill="none" stroke="#0f9141" stroke-width="2.5"/></svg>
  </div>
</section>

<section>
  <div class="abs produce-title"><h2 class="heading"><em>We</em> Produce</h2></div>
  <div class="abs product" style="left:120px;top:2316px">
    <div class="product-photo" style="background:linear-gradient(160deg,#777 0%,#3e3f40 50%,#2a7f9a 100%)" role="img" aria-label="Gloved hand scooping tire derived fuel chips"></div>
    <div class="product-bar">TIRE DERIVED FUEL
      <svg width="32" height="24" viewBox="0 0 32 24"><path d="M2 12h27M20 3l9 9-9 9" fill="none" stroke="#fff" stroke-width="2.5"/></svg>
    </div>
  </div>
  <div class="abs product" style="left:621px;top:2316px">
    <div class="product-photo" style="background:linear-gradient(160deg,#d9d4cc 0%,#8a7558 45%,#4d3d2b 100%)" role="img" aria-label="Coil of clean steel tire wire beside a bead cutting tool"></div>
    <div class="product-bar" style="padding-left:42px">CLEAN TIRE WIRE &amp;<br>FURTHER MATERIALS
      <svg width="32" height="24" viewBox="0 0 32 24"><path d="M2 12h27M20 3l9 9-9 9" fill="none" stroke="#fff" stroke-width="2.5"/></svg>
    </div>
  </div>
</section>

<section>
  <div class="abs blog"></div>
  <div class="abs blog-title"><h2 class="heading"><em>Latest</em> Blog</h2></div>

  <article class="abs post" style="left:111px;top:2867px">
    <div class="post-photo" style="background:linear-gradient(160deg,#b6d86b 0%,#6aa22d 45%,#3b3b34 100%)" role="img" aria-label="Old tire lying in tall green grass"></div>
    <div class="post-date">27<br>Apr</div>
    <h4>Nemo enim ipsam voluptatem quia voluptas sit asperna</h4>
    <span class="tag">Lorem Ipsum</span>
    <p>Nemo enim ipsam voluptatem quia voluptas sit asarna. Nemo enim ipsam voluptatem quiaty voluptas sit asperna.</p>
  </article>
  <article class="abs post" style="left:443px;top:2867px">
    <div class="post-photo" style="background:radial-gradient(circle at 45% 65%,#d8b8a4 0%,#2f5a3a 35%,#1b3a24 100%)" role="img" aria-label="Hand holding green rubber crumb"></div>
    <div class="post-date">27<br>Apr</div>
    <h4>Nemo enim ipsam voluptatem quia voluptas sit asperna</h4>
    <span class="tag">Lorem Ipsum</span>
    <p>Nemo enim ipsam voluptatem quia voluptas sit asarna. Nemo enim ipsam voluptatem quiaty voluptas sit asperna.</p>
  </article>
  <article class="abs post" style="left:774px;top:2867px">
    <div class="post-photo" style="background:linear-gradient(160deg,#6d6a60 0%,#4b4a43 50%,#8a6a3a 100%)" role="img" aria-label="Field of scrap tires with a loader"></div>
    <div class="post-date">27<br>Apr</div>
    <h4>Nemo enim ipsam voluptatem quia voluptas sit asperna</h4>
    <span class="tag">Lorem Ipsum</span>
    <p>Nemo enim ipsam voluptatem quia voluptas sit asarna. Nemo enim ipsam voluptatem quiaty voluptas sit asperna.</p>
  </article>
</section>

<footer>
  <div class="abs footer-divider"></div>
  <div class="abs footer"></div>
  <div class="abs footer-brand">GravaLoop</div>
  <div class="abs subscribe"><span>Enter Email ID</span><b>Learn More</b></div>
  <div class="abs rule" style="left:111px;top:3651px;width:977px"></div>

  <div class="abs col-title" style="left:139px">Contact</div>
  <svg class="abs" style="left:139px;top:3728px" width="20" height="26" viewBox="0 0 20 26"><path d="M10 24s8-8 8-14a8 8 0 0 0-16 0c0 6 8 14 8 14z" fill="none" stroke="#0f9141" stroke-width="1.8"/><circle cx="10" cy="10" r="3" fill="none" stroke="#0f9141" stroke-width="1.8"/></svg>
  <div class="abs contact-line" style="left:172px;top:3722px">GravaLoop<br>Address Comes Here</div>
  <svg class="abs" style="left:139px;top:3806px" width="22" height="22" viewBox="0 0 22 22"><path d="M5 2l4 4-2 3c1 3 3 5 6 6l3-2 4 4-3 3C9 20 2 13 2 5z" fill="none" stroke="#0f9141" stroke-width="1.6"/></svg>
  <div class="abs contact-line" style="left:172px;top:3805px"><b style="font-weight:600">Phone:</b><br>+1 555-014-2290</div>

  <div class="abs vrule" style="left:392px"></div>
  <div class="abs col-title" style="left:463px">Quick Links</div>
  <ul class="abs links" style="left:463px">
    <li>Home</li><li>About</li><li>Services</li><li>We Provide</li><li>Latest Blog</li>
  </ul>

  <div class="abs vrule" style="left:656px"></div>
  <div class="abs col-title" style="left:718px">Other Links</div>
  <ul class="abs links" style="left:718px">
    <li>Privacy Policy</li><li>Tearms &amp; comditions</li><li>Cookies</li>
  </ul>

  <div class="abs vrule" style="left:942px"></div>
  <div class="abs social" style="top:3678px" aria-label="Social profile"></div>
  <div class="abs social" style="top:3732px" aria-label="Social profile"></div>
  <div class="abs social" style="top:3786px" aria-label="Social profile"></div>
  <div class="abs social" style="top:3840px" aria-label="Social profile"></div>

  <div class="abs rule" style="left:111px;top:3917px;width:977px"></div>
  <div class="abs copyright">2022 GravaLoop. All Rights Reserved.</div>
</footer>

</body>
</html>
```